Einladungskarten für Benefizveranstaltung
Zielgruppe
vorrangig Unternehmer;
Privatpersonen
Sportbegeisterte
Aufgabenstellung
Wir benötigen für eine Veranstaltung mit 3 Terminen an 3 vers. Standorten zwei Einladungskarten.
1.) off. Einladung & 2.) VIP-Einladung
Bei der Veranstaltung handelt es sich um einen Vortrag des blinden Bergsteigers Timo Brandler, der alle Seven Summits (die höchsten Gifpel der Kontinente) erreichen möchte. www.timobrandler-vortrag.com
Die Betriebs-Forum unterstützt ihn dabei und braucht die Hilfe von anderen Unternehmen & Privatpersonen. Diese werden zur Veranstaltung eingeladen.
Das Design der Einladungskarten soll an unser Corporate Design angepasst werden (www.betriebs-forum.eu) aber auch den Aspekt "Bergsteigen, Natur, Timo Brandler" beinhalten.

```html
<!DOCTYPE html>
<html lang="de">
<head>
<meta charset="utf-8">
<title>Balanceakt – Betriebs-Forum 2011 Einladung</title>
<link href="https://fonts.googleapis.com/css2?family=Source+Sans+3:wght@400;600;700&display=swap" rel="stylesheet">
<style>
:root{
  --orange:#e2601e;
  --grey:#8c8c8c;
  --text:#5a5a5a;
  --line:#c9c9c9;
  --sky-top:#1f4f8f;
  --sky-mid:#5f86bb;
  --snow:#eef2f7;
  --stage:#ececec;
  --paper:#ffffff;
}
*{box-sizing:border-box;margin:0;padding:0}
html,body{width:1200px;height:1200px;overflow:hidden}
body{background:var(--stage);font-family:"Source Sans 3",Arial,sans-serif;color:var(--text);position:relative}
.card{position:absolute;background:var(--paper);overflow:hidden}
.brand{display:flex;align-items:center;gap:8px;font-weight:600;color:var(--grey);white-space:nowrap}
.brand-mark{background:var(--orange);flex:none}
.accent{color:var(--orange)}

/* Cover */
.cover{left:200px;top:24px;width:380px;height:537px}
.cover .brand{position:absolute;right:28px;top:80px;font-size:22px}
.cover .brand-mark{width:16px;height:16px}
.cover-tagline{position:absolute;left:28px;top:162px;font-size:16px;color:var(--orange)}
.cover-photo{position:absolute;left:0;top:186px;width:380px;height:351px;
  background:linear-gradient(180deg,var(--sky-top) 0%,var(--sky-mid) 30%,#b9c9de 48%,#dfe6ef 62%,var(--snow) 100%)}
.cover-title{position:absolute;left:28px;top:204px;color:#fff}
.cover-title h1{font-size:29px;font-weight:700;letter-spacing:.5px;line-height:1}
.cover-title h1 .accent{color:var(--orange)}
.cover-title .event{font-size:16px;margin-top:3px}
.cover-title .dates{font-size:9.5px;margin-top:6px;letter-spacing:.2px}

/* Spread */
.spread{left:220px;top:601px;width:760px;height:537px}
.photo-strip{position:absolute;left:0;top:0;width:576px;height:102px;display:flex;border-bottom-right-radius:14px;overflow:hidden}
.photo-strip div{flex:1}
.ph1{background:linear-gradient(160deg,#c9d9ec,#8aa9cf)}
.ph2{background:linear-gradient(180deg,#2f62a6,#d8e3ef)}
.ph3{background:linear-gradient(150deg,#8c8c86,#c8c4bb)}
.ph4{background:linear-gradient(150deg,#6d6a64,#a8a59e)}
.spread-brand{position:absolute;left:596px;top:34px;display:flex;align-items:flex-start;gap:7px}
.spread-brand .brand-mark{width:12px;height:12px;margin-top:3px}
.spread-brand .name{display:block;font-size:14px;font-weight:600;color:var(--orange);line-height:1.2;white-space:nowrap}
.spread-brand .slogan{display:block;font-size:9px;font-style:normal;font-weight:600;color:var(--grey);line-height:1.3;margin-top:2px}
.page-left{position:absolute;left:35px;top:124px;width:330px;font-size:9.5px;line-height:1.42}
.page-left p{margin-bottom:9px}
.map{position:absolute;left:200px;top:392px;width:170px;height:120px;background:linear-gradient(135deg,#f3f3f3,#e4e4e4);border-radius:4px}
.page-right{position:absolute;left:430px;top:124px;width:300px;font-size:9.5px;line-height:1.42}
.page-right h3{font-size:10px;font-weight:600;color:var(--orange);margin:10px 0 2px}
.page-right h3:first-child{margin-top:0}
.rows div{display:flex}
.rows span:first-child{width:46px;flex:none}
.thanks{position:absolute;left:430px;top:410px;font-size:9.5px;color:var(--orange)}
.sponsors{position:absolute;left:430px;top:436px;width:310px;display:grid;grid-template-columns:repeat(3,auto);justify-content:start;row-gap:18px;column-gap:18px}
.sponsor{display:flex;align-items:center;gap:5px;font-size:9px;font-weight:600;color:var(--grey);white-space:nowrap}
.sponsor i{width:11px;height:11px;background:var(--line);flex:none}

/* Reply form */
.reply{left:620px;top:24px;width:380px;height:537px}
.fax{position:absolute;left:28px;top:34px;font-size:16px;color:var(--grey)}
.fax .accent{font-weight:600}
.choice{position:absolute;left:28px;top:98px;font-size:9.5px;line-height:1.8}
.choice .opts span{margin-right:18px}
.form-area{position:absolute;left:0;top:178px;width:353px;height:232px;background:linear-gradient(180deg,#f1f1f1,#fafafa)}
.field-grid{position:absolute;left:28px;top:184px;width:310px}
.field-row{display:flex;height:32px;border-bottom:1px solid var(--line);font-size:7.5px;color:var(--orange)}
.field-row span{flex:1;padding-top:4px}
.side-photo{position:absolute;right:0;top:190px;width:27px;height:347px;border-top-left-radius:10px;background:linear-gradient(180deg,var(--sky-top),var(--sky-mid) 45%,#dfe6ef)}
.reply-info{position:absolute;left:28px;top:420px;font-size:8px;line-height:1.5;width:300px}
.reply-info .org{margin-top:10px}
.reply .brand{position:absolute;right:42px;bottom:24px;font-size:10px}
.reply .brand-mark{width:9px;height:9px}
</style>
</head>
<body>

<section class="card cover">
  <div class="brand"><span>Betriebs-Forum GmbH</span><span class="brand-mark"></span></div>
  <p class="cover-tagline">Timo Brandler – blind climber</p>
  <div class="cover-photo" role="img" aria-label="Verschneites Hochgebirgspanorama unter blauem Himmel mit einer Gipfellinie der Seven Summits: Kosciuszko, Mt Vinson, Mt Elbrus, Kilimanjaro, Denali, Aconcagua, Mt Everest"></div>
  <div class="cover-title">
    <h1>BALANCE<span class="accent">AKT</span></h1>
    <p class="event">Betriebs-Forum 2011</p>
    <p class="dates">20.Juni GRAZ – 21.Juni WIEN – 30. Juni INNSBRUCK</p>
  </div>
</section>

<section class="card reply">
  <p class="fax"><span class="accent">Anmeldefax</span> +43 512 400700 20</p>
  <div class="choice">
    <p class="accent">Ich nehme an folgender Veranstaltung teil:</p>
    <p class="opts"><span>O 20.06. GRAZ</span><span>O 21.06. WIEN</span><span>O 30.06. INNSBRUCK</span></p>
    <p>O Ich werde in Begleitung kommen</p>
  </div>
  <div class="form-area"></div>
  <div class="field-grid">
    <div class="field-row"><span>Titel</span><span>Nachname</span><span>Vorname</span></div>
    <div class="field-row"><span>Straße/Nr.</span><span>PLZ/Ort</span></div>
    <div class="field-row"><span>Unternehmen</span></div>
    <div class="field-row"><span>E-Mail</span></div>
    <div class="field-row"><span>Telefon</span><span>Fax</span></div>
    <div class="field-row"><span>Datum</span><span>Unterschrift</span></div>
  </div>
  <div class="side-photo" role="img" aria-label="Ausschnitt eines blauen Berghimmels über Schnee"></div>
  <div class="reply-info">
    <p>Aufgrund der begrenzten Teilnehmerzahl bitten wir um verbindliche Anmeldung bis <span class="accent">Freitag, 17. Juni 2011</span>:</p>
    <p>Telefon: +43 512 400700 | Fax: +43 512 400700 20</p>
    <p>E-Mail: anmeldung@betriebs-forum.at | Web: www.betriebs-forum.at</p>
    <p class="org"><span class="accent">Veranstalter</span><br>Betriebs-Forum GmbH | Bergweg 12 | 6020 Innsbruck</p>
  </div>
  <div class="brand"><span>Betriebs-Forum</span><span class="brand-mark"></span></div>
</section>

<section class="card spread">
  <div class="photo-strip">
    <div class="ph1" role="img" aria-label="Porträt des Bergsteigers mit Gletscherbrille im Schnee"></div>
    <div class="ph2" role="img" aria-label="Seilschaft am Gipfel vor blauem Himmel"></div>
    <div class="ph3" role="img" aria-label="Kletterer an einer Felswand"></div>
    <div class="ph4" role="img" aria-label="Kletterer mit Helm im Fels"></div>
  </div>
  <div class="spread-brand">
    <span class="brand-mark"></span>
    <div>
      <span class="name">Betriebs-Forum</span>
      <em class="slogan">gemeinsam stark.</em>
    </div>
  </div>

  <div class="page-left">
    <p><span class="accent">Der Osttiroler, Timo Johann Brandler,</span> 44, ist von Geburt an blind. Seit seinem neunten Lebensjahr geht er seiner großen Leidenschaft, dem Klettern, nach und bewältigt auf diese Weise Touren im höchsten Schwierigkeitsgrad. Herzensprojekt ist es, als erster blinder Europäer die 7-Summits – die sieben höchsten Gipfel der Kontinente – zu erreichen. Schon sechs dieser legendären Bergriesen durfte er mit Händen und Füßen berühren.</p>
    <p><span class="accent">Den krönenden Abschluss</span> jedoch soll im Frühjahr 2012 die Besteigung des Mount Everest bilden. Zur Verwirklichung dieses Vorhabens braucht Timo Brandler verlässliche Partner. Denn am Berg – genau wie im Leben – sind Erfolge ohne eine funktionierende Seilschaft nicht möglich. Jeder Schritt ist von Vertrauen in die Partner abhängig, gerade in ungewohntem Gelände.</p>
    <p>Seine Mut, Willenskraft, Professionalität und Ausdauer machen ihn zum idealen Botschafter der Unternehmen, die ihn bei seinem einzigartigen Projekt begleiten und dieser Herausforderung gemeinsam mit ihm begegnen.</p>
  </div>
  <div class="map" role="img" aria-label="Weltkarte mit markierten Gipfeln Mt Elbrus, Mt Everest, Kilimanjaro und Kosciuszko"></div>

  <div class="page-right">
    <h3>Termine</h3>
    <div class="rows">
      <div><span>20.06.2011</span><span>&nbsp;Veranstaltungszentrum Graz</span></div>
      <div><span>21.06.2011</span><span>&nbsp;Veranstaltungszentrum Wien</span></div>
      <div><span>30.06.2011</span><span>&nbsp;Veranstaltungszentrum Innsbruck</span></div>
    </div>
    <h3>Programm</h3>
    <div class="rows">
      <div><span>16:00Uhr</span><span>Begrüßung</span></div>
      <div><span>16:15Uhr</span><span>Timo Brandler – „Blind auf die Gipfel der Welt“</span></div>
      <div><span>18:15Uhr</span><span>Get Together am Buffet</span></div>
    </div>
    <h3>Teilnahmegebühr</h3>
    <p>€ 35,- pro Teilnehmer. Anmeldungen werden in der Reihenfolge des Eintreffens und nach Maßgabe freier Plätze berücksichtigt. Wir ersuchen Sie, nach Erhalt der Rechnung die Teilnahmegebühr umgehend zu überweisen.</p>
    <h3>Ermäßigung</h3>
    <p>Bei Anmeldung &amp; Bezahlung über <strong>www.betriebs-forum.at</strong> verringert sich die Teilnahmegebühr auf € 30,-</p>
  </div>
  <p class="thanks">Vielen Dank an jene Unternehmen, die Timo Brandler unterstützen</p>
  <div class="sponsors">
    <div class="sponsor"><i></i>Handwerk Nord</div>
    <div class="sponsor"><i></i>Alpenlicht</div>
    <div class="sponsor"><i></i>Talfahrt Motors</div>
    <div class="sponsor"><i></i>Atelier Sommer</div>
    <div class="sponsor"><i></i>Ing. Moser Beratung</div>
  </div>
</section>

</body>
</html>
```